New Record Label needs a Web design

We are Moss Lantern: a London based, new & independent music production company aimed at the 25-40 age group. The musical style is Soul/Classic Motown.
We have at the moment just one signed artist, but will expand in the future.
We dont' have any webpage yet and are looking for an innovative web design for our webpage www.moss-lantern.com
I have uploaded our company logo.

Initially the whole website will only have 3 tabs: Home page/Artists/Contact

The design should be classic and high-end, but can be a bit crazy too.

```html
<!DOCTYPE html>
<html lang="en">
<head>
<meta charset="utf-8">
<title>Moss Lantern — New &amp; Independent Music Production Company</title>
<link href="https://fonts.googleapis.com/css2?family=Bebas+Neue&family=Montserrat:wght@400;500&family=Open+Sans:wght@400;600&display=swap" rel="stylesheet">
<style>
  :root{
    --red:#e2302c;
    --red-deep:#b8322c;
    --peach:#f4c9b8;
    --ink:#111111;
    --charcoal:#2b2b2b;
    --grey-text:#6b6b6b;
    --white:#ffffff;
    --footer:#0c0c0c;
  }
  *{margin:0;padding:0;box-sizing:border-box}
  html,body{width:1200px;height:2179px;overflow:hidden}
  body{position:relative;background:var(--white);font-family:"Open Sans",Arial,sans-serif;color:var(--charcoal)}
  .abs{position:absolute}

  /* Hero */
  .hero{left:0;top:0;width:1200px;height:626px;
    background:radial-gradient(ellipse at 62% 35%,#5a5a5a 0%,#2e2e2e 40%,#141414 80%);}
  .hero-topline{left:0;top:0;width:1200px;height:6px;background:var(--red)}
  .brand{left:100px;top:20px;width:192px;height:192px;border-radius:50%;
    background:radial-gradient(circle at 50% 40%,#f5f0ef 0%,#c7a9a6 60%,#8c6a66 100%);
    display:flex;align-items:center;justify-content:center}
  .brand-name{font-family:"Montserrat",sans-serif;font-weight:500;font-size:22px;color:var(--red)}
  .nav{top:102px;left:0;width:1200px;font-family:"Montserrat",sans-serif;font-size:19px;color:var(--white)}
  .nav a{position:absolute;color:var(--white);text-decoration:none}
  .nav .sep{position:absolute;color:var(--red)}
  .hero-title{left:102px;top:286px;font-family:"Bebas Neue",sans-serif;font-size:50px;line-height:61px;color:var(--white);letter-spacing:.5px}
  .dots{top:592px;left:565px;display:flex;gap:10px}
  .dots span{width:11px;height:11px;border-radius:50%;background:var(--white)}
  .dots span.active{background:var(--red)}

  /* Intro */
  .intro-heading{top:652px;left:0;width:1200px;text-align:center;font-family:"Montserrat",sans-serif;font-size:24px;color:var(--red)}
  .intro-text{top:700px;left:130px;width:940px;text-align:center;font-size:14px;line-height:24px;color:var(--grey-text)}

  .service{width:300px;text-align:center}
  .service-icon{display:block;margin:0 auto}
  .service-title{margin-top:18px;font-family:"Montserrat",sans-serif;font-size:19px;color:var(--ink)}
  .service-text{margin-top:8px;font-size:13.5px;line-height:23px;color:var(--grey-text)}
  .read-more{display:block;margin-top:2px;font-size:13.5px;color:var(--red);text-decoration:none}

  /* Artists */
  .artists{left:0;top:1093px;width:1200px;height:270px;
    background:radial-gradient(ellipse at 50% 60%,#2a2a2a 0%,#0b0b0b 70%)}
  .artists-title{top:1117px;left:0;width:1200px;text-align:center;font-family:"Montserrat",sans-serif;font-size:24px;color:var(--white)}
  .artist{top:1168px;width:160px;height:157px;border:3px solid var(--white)}

  /* Call to action */
  .cta-heading{top:1386px;left:0;width:1200px;text-align:center;font-family:"Montserrat",sans-serif;font-size:38px;color:var(--red)}
  .cta-text{top:1452px;left:100px;width:985px;text-align:center;font-size:14.5px;line-height:30px;color:var(--ink)}
  .btn{top:1533px;width:236px;height:54px;border-radius:3px;font-family:"Montserrat",sans-serif;font-size:19px;color:var(--white);display:flex;align-items:center;justify-content:center}
  .btn-red{left:328px;background:linear-gradient(#ef4a44,#cf2824)}
  .btn-dark{left:588px;background:linear-gradient(#4a4a4a,#262626)}

  /* Contact */
  .contact{left:0;top:1629px;width:1200px;height:465px;
    background:radial-gradient(ellipse at 50% 50%,#d34a40 0%,#b23129 60%,#9d2a24 100%)}
  .contact-title{top:1652px;left:0;width:1200px;text-align:center;font-family:"Montserrat",sans-serif;font-size:34px;color:var(--white)}
  .field{left:100px;width:403px;background:var(--white);font-size:14px;color:#9a9a9a;padding:17px 13px 0}
  .submit{left:100px;top:2008px;width:403px;height:45px;border-radius:3px;background:linear-gradient(#2f2f2f,#0f0f0f);
    color:var(--white);font-family:"Montserrat",sans-serif;font-size:16px;display:flex;align-items:center;justify-content:center}
  .map{left:561px;top:1727px;width:539px;height:326px;border:2px solid var(--white);
    background:linear-gradient(135deg,#ebe6dc 0%,#e0dccf 50%,#f1e7b5 100%)}

  /* Footer */
  .footer{left:0;top:2094px;width:1200px;height:85px;background:var(--footer)}
  .copyright{top:2126px;left:102px;font-size:14.5px;color:var(--white)}
  .social{top:2118px;width:32px;height:32px}
</style>
</head>
<body>

<header>
  <div class="abs hero" role="img" aria-label="Black and white photo of a studio microphone over a mixing desk"></div>
  <div class="abs hero-topline"></div>
  <div class="abs brand"><span class="brand-name">Moss Lantern</span></div>
  <nav class="abs nav">
    <a href="#" style="left:760px">Home</a>
    <span class="sep" style="left:843px">/</span>
    <a href="#" style="left:886px">Artists</a>
    <span class="sep" style="left:975px">/</span>
    <a href="#" style="left:1017px">Contact</a>
  </nav>
  <h1 class="abs hero-title">New &amp; Independent<br>Music Production Company</h1>
  <div class="abs dots"><span class="active"></span><span></span><span></span></div>
</header>

<section>
  <h2 class="abs intro-heading">World Class Production Company Specializing In&nbsp; Music Production</h2>
  <p class="abs intro-text">Lorem ipsum dolor sit amet, consectetuer adipiscing elit. Aenean commodo ligula eget dolor. Aenean massa. Cum sociis natoque penatibus et .magnis dis parturient montes, nascetur ridiculus mus. Donec quam felis, ultricies nec, pellentesque eu, pretium quis, sem</p>

  <div class="abs service" style="left:126px;top:782px">
    <svg class="service-icon" width="140" height="130" viewBox="0 0 140 130">
      <path d="M88 6 A60 60 0 0 1 132 66 A60 60 0 0 1 72 126 A60 60 0 0 1 14 86" fill="none" stroke="var(--peach)" stroke-width="9"/>
      <circle cx="70" cy="66" r="60" fill="var(--red)"/>
      <path d="M46 78 V64 a24 24 0 0 1 48 0 V78" fill="none" stroke="#fff" stroke-width="7"/>
      <rect x="42" y="66" width="14" height="22" rx="4" fill="#fff"/>
      <rect x="84" y="66" width="14" height="22" rx="4" fill="#fff"/>
    </svg>
    <h3 class="service-title">Trusted Audio Solutions</h3>
    <p class="service-text">Lorem ipsum dolor sit amet, consectetuer adipiscing elit. Aenean commodo ligula eget dolor. Aenean massa.</p>
    <a class="read-more" href="#">Read More +</a>
  </div>

  <div class="abs service" style="left:443px;top:782px">
    <svg class="service-icon" width="140" height="130" viewBox="0 0 140 130">
      <path d="M52 6 A60 60 0 0 0 8 66 A60 60 0 0 0 68 126" fill="none" stroke="var(--peach)" stroke-width="9"/>
      <circle cx="72" cy="66" r="60" fill="var(--red)"/>
      <path d="M62 84 V46 L92 40 V78" fill="none" stroke="#fff" stroke-width="6"/>
      <ellipse cx="56" cy="85" rx="9" ry="7" fill="#fff"/>
      <ellipse cx="86" cy="79" rx="9" ry="7" fill="#fff"/>
    </svg>
    <h3 class="service-title">Complete Post production Services</h3>
    <p class="service-text">Lorem ipsum dolor sit amet, consectetuer adipiscing elit. Aenean commodo ligula eget dolor. Aenean massa.</p>
    <a class="read-more" href="#">Read More +</a>
  </div>

  <div class="abs service" style="left:765px;top:782px">
    <svg class="service-icon" width="140" height="130" viewBox="0 0 140 130">
      <path d="M88 6 A60 60 0 0 1 132 66" fill="none" stroke="var(--peach)" stroke-width="9"/>
      <path d="M14 86 A60 60 0 0 1 30 22" fill="none" stroke="var(--peach)" stroke-width="9"/>
      <circle cx="70" cy="66" r="60" fill="var(--red)"/>
      <path d="M44 56 H56 L72 42 V90 L56 76 H44 Z" fill="#fff"/>
      <path d="M80 56 a12 12 0 0 1 0 20 M86 48 a22 22 0 0 1 0 36" fill="none" stroke="#fff" stroke-width="5" stroke-linecap="round"/>
    </svg>
    <h3 class="service-title">Sonic Branding</h3>
    <p class="service-text">Lorem ipsum dolor sit amet, consectetuer adipiscing elit. Aenean commodo ligula eget dolor. Aenean massa.</p>
    <a class="read-more" href="#">Read More +</a>
  </div>
</section>

<section>
  <div class="abs artists" role="img" aria-label="Dark recording studio background"></div>
  <h2 class="abs artists-title">Our Artists</h2>
  <div class="abs artist" style="left:131px;background:linear-gradient(#e9e6e3,#cfc8c2 60%,#1d1d1d 61%)" role="img" aria-label="Artist portrait"></div>
  <div class="abs artist" style="left:327px;background:linear-gradient(#cfc9c6,#b39a8a 55%,#2d2a28)" role="img" aria-label="Artist portrait"></div>
  <div class="abs artist" style="left:522px;background:linear-gradient(#f1f1f1,#c79d82 55%,#6c7280)" role="img" aria-label="Artist portrait"></div>
  <div class="abs artist" style="left:716px;background:linear-gradient(#f3ecc6,#e6d59c 55%,#c2a07e)" role="img" aria-label="Artist portrait"></div>
  <div class="abs artist" style="left:905px;background:linear-gradient(#8b5040,#5a3428 60%,#2b1c17)" role="img" aria-label="Artist portrait"></div>
</section>

<section>
  <h2 class="abs cta-heading">Lorem Ipsum</h2>
  <p class="abs cta-text">Working as a webcam entertainer can be a very lucrative business, whether it is your only job or something you do on the side. It gives you the flexibility to create your own schedule based around your availability.</p>
  <a class="abs btn btn-red" href="#">What do I need?</a>
  <a class="abs btn btn-dark" href="#">How do I sign up?</a>
</section>

<section>
  <div class="abs contact" role="img" aria-label="Red tinted photo of mixing desk faders"></div>
  <h2 class="abs contact-title">Contact Us</h2>
  <div class="abs field" style="top:1727px;height:54px">Your Name</div>
  <div class="abs field" style="top:1800px;height:54px">Your Email</div>
  <div class="abs field" style="top:1873px;height:120px;padding-top:14px">Message</div>
  <div class="abs submit">Submit</div>
  <div class="abs map" role="img" aria-label="Street map showing the studio location"></div>
</section>

<footer>
  <div class="abs footer"></div>
  <p class="abs copyright">© 2014 Moss Lantern All Rights Reserved</p>
  <div class="abs social" style="left:918px;background:#3b5a9a"></div>
  <div class="abs social" style="left:968px;background:#2aa3d8"></div>
  <div class="abs social" style="left:1018px;background:#d6d6d6"></div>
  <div class="abs social" style="left:1069px;background:#1f7bb6"></div>
</footer>

</body>
</html>
```